Filmproduktion braucht Visitenkarten und Briefpapier
Zielgruppe
Wir sind eine junge Filmproduktion Firma mit dem Namen Lichtkante.
Unser Kerngeschäft sind Image und Unternehmensfilme, sowie Event und Messefilme.
Aufgabenstellung
Wir sind junge, kreative, Filmschaffende und das soll sich auch in der Visitenkarte widerspiegeln, dennoch macht bitte auch ein paar klassische Vorschläge, manchmal ist weniger mehr.
Unser altes Briefpapier ist angehängt. Das neue Briefpapier muss von uns veränderbar sein, da wir noch nicht alle Daten haben wie Steuernummer und USt-ID, bitte aber schon als Dummy anlegen.
Unsere alten Visitenkarten sind angehängt, diese Daten Stimmen, aber ansonsten stimmt daran nix, wie wir finden. Bitte nicht daran Orientieren!!!
Bitte bei der Adresse Lichtkante GbR schreiben.
Unser neues Logo, jetzt in blau ist ebenfalls angehängt.
Viel Spass beim Designen.

```html
<!DOCTYPE html>
<html lang="de">
<head>
<meta charset="utf-8">
<title>Lichtkante GbR – Briefpapier und Visitenkarte</title>
<link rel="stylesheet" href="https://fonts.googleapis.com/css2?family=Hind:wght@400;500&family=Kalam:wght@300&display=swap">
<style>
  :root {
    --stage: #737277;
    --paper: #ffffff;
    --card: #efeee4;
    --brand-blue: #5592cf;
    --ink: #222222;
    --mark: #a6a6a6;
  }
  * { margin: 0; padding: 0; box-sizing: border-box; }
  html, body {
    width: 960px; height: 1200px; overflow: hidden;
    background: var(--stage);
    font-family: "Hind", "Helvetica Neue", Arial, sans-serif;
    color: var(--ink);
  }
  .canvas { position: relative; width: 960px; height: 1200px; }
  .letter-sheet {
    position: absolute; left: 77px; top: 0; width: 803px; height: 1200px;
    background: var(--paper);
  }
  .letter-brand {
    position: absolute; left: 77px; top: 82px; width: 803px;
    text-align: center;
  }
  .letter-brand__dot {
    display: block; margin: 0 auto 26px; width: 64px; height: 64px;
    border-radius: 50%; background: var(--brand-blue);
  }
  .letter-brand__name {
    font-size: 18px; font-weight: 400; letter-spacing: 0.62em;
    padding-left: 0.62em; color: var(--ink); line-height: 20px;
  }
  .return-line {
    position: absolute; left: 171px; top: 222px;
    font-size: 7px; color: #444; white-space: nowrap;
  }
  .accent { color: var(--brand-blue); }
  .fold-mark {
    position: absolute; left: 77px; top: 437px; width: 18px; height: 1px;
    background: var(--mark);
  }
  .punch-mark {
    position: absolute; left: 77px; top: 597px; width: 0; height: 0;
    border-top: 5px solid transparent; border-bottom: 5px solid transparent;
    border-left: 8px solid var(--mark);
  }
  .card-preview { position: absolute; left: 0; top: 0; }
  .card-preview text { font-family: "Hind", "Helvetica Neue", Arial, sans-serif; }
  .card-preview .signature { font-family: "Kalam", cursive; font-weight: 300; }
  .letter-footer {
    position: absolute; left: 150px; top: 1084px; width: 670px;
    font-size: 11.4px; line-height: 18px; text-align: justify;
    hyphens: auto; -webkit-hyphens: auto;
    text-indent: 50px; color: var(--ink);
  }
</style>
</head>
<body>
<div class="canvas">
  <div class="letter-sheet"></div>

  <header class="letter-brand">
    <span class="letter-brand__dot"></span>
    <div class="letter-brand__name">LICHTKANTE</div>
  </header>

  <p class="return-line"><span class="accent">LICHTKANTE GbR</span> &nbsp;· Filmproduktion · Lichthofstraße 7 · 10999 Berlin</p>

  <span class="fold-mark"></span>
  <span class="punch-mark"></span>

  <svg class="card-preview" width="960" height="1200" viewBox="0 0 960 1200">
    <defs>
      <clipPath id="card-back-shape">
        <polygon points="579,453 880,435 880,650 594,670"/>
      </clipPath>
      <clipPath id="card-front-shape">
        <rect x="458" y="310" width="331" height="214"/>
      </clipPath>
    </defs>

    <g class="card-back" clip-path="url(#card-back-shape)">
      <polygon points="579,453 880,435 880,650 594,670" fill="var(--brand-blue)"/>
      <g transform="rotate(-3.6 560 592)" fill="#ffffff">
        <text class="signature" x="534" y="592" font-size="27">Jonas Reiter</text>
        <text x="645" y="622" font-size="9.4">Und hier könnte ein fortlaufender Infotext zu Filmproduktionen</text>
        <text x="645" y="636" font-size="9.4">stehen, was LICHTKANTE leistet, in welchen Sparten Sie arbeitet</text>
        <text x="645" y="650" font-size="9.4">beitet, und wer eventuell für was Ansprechpartner ist.</text>
      </g>
    </g>

    <g class="card-front">
      <rect x="458" y="310" width="331" height="214" fill="var(--card)"/>
      <circle cx="617" cy="372" r="20" fill="var(--brand-blue)"/>
      <text x="620" y="427" font-size="12" letter-spacing="5.5" text-anchor="middle" fill="var(--ink)">LICHTKANTE</text>
      <g clip-path="url(#card-front-shape)">
        <text class="signature" x="720" y="450" font-size="27" fill="var(--ink)">Jonas Reiter</text>
      </g>
      <text x="484" y="477" font-size="8.2" fill="var(--ink)">Lichtkante GbR, Lichthofstraße 7, 10999 Berlin <tspan fill="var(--brand-blue)">TELEFON</tspan> 01234 / 567 890-10 <tspan fill="var(--brand-blue)">FAX</tspan> -12</text>
      <text x="484" y="491" font-size="8.2" fill="var(--ink)"><tspan fill="var(--brand-blue)">GESCHÄFTSFÜHRUNG</tspan> Lukas Brandt, Felix Sommer, Jonas Reiter</text>
      <text x="484" y="505" font-size="8.2" fill="var(--ink)"><tspan fill="var(--brand-blue)">MAIL</tspan> produktion@lichtkante.example <tspan fill="var(--brand-blue)">WEB</tspan> www.lichtkante.example</text>
    </g>
  </svg>

  <footer class="letter-footer">
    <span class="accent">LICHTKANTE GbR</span> Filmproduktion, Lichthofstraße 7, 10999 Berlin <span class="accent">WEB</span> www.lichtkante.example <span class="accent">MAIL</span> produktion@lichtkante.example <span class="accent">TELEFON</span> 01234 / 567 890 10 <span class="accent">FAX</span> 01234 / 567 890 12 <span class="accent">GESCHÄFTSFÜHRUNG</span> Lukas Brandt, Felix Sommer, Jonas Reiter <span class="accent">BANKVERBINDUNG</span> Spreeufer Bank, IBAN: DE00100100001234567890, BIC: LKBADE2BXXX <span class="accent">STEUERNUMMER</span> 00/000/00000 <span class="accent">UST-ID</span> DE000000000, Filmproduktion für Image, Unternehmen, Event- und Messefilm.
  </footer>
</div>
</body>
</html>
```